Business Card and Stationary Designs for commercial construction company
Halvern Builders, Inc.
Creative Brief
Use standard fonts
Dennis Whitlock
Director of Operations
6387 Larkmeadow Lane Elk Grove, CA 95731
dennis.whitlock@halvernbldg.com
License #3084519
We like the colors of our logo, so please incorporate them into the card. The font for the other information on the business card does not have to match the logo font, but it should coordinate with it. We need the stationary design to be used to print actual stationary, but we would also like a word document that we can use for creating letters on electronic stationary.

```html
<!DOCTYPE html>
<html lang="en">
<head>
<meta charset="utf-8">
<title>Halvern Builders – Business Card</title>
<link rel="stylesheet" href="https://fonts.googleapis.com/css2?family=Montserrat:wght@800&family=Open+Sans:wght@400;600;700&display=swap">
<style>
  :root {
    --bg: #8a8a8a;
    --brand-red: #e0222b;
    --card-white: #ffffff;
    --ink: #333333;
    --ink-soft: #6b6b6b;
    --rule-grey: #bdbdbd;
  }
  * { box-sizing: border-box; margin: 0; padding: 0; }
  html, body { width: 1200px; height: 908px; overflow: hidden; }
  body {
    background: var(--bg);
    font-family: "Open Sans", Arial, sans-serif;
    position: relative;
  }
  .card {
    position: absolute;
    top: 302px;
    width: 530px;
    height: 304px;
    border-radius: 22px;
    overflow: hidden;
  }
  .card--front {
    left: 45px;
    background: var(--brand-red);
    display: flex;
    align-items: center;
    justify-content: center;
  }
  .card--back {
    left: 625px;
    background: var(--card-white);
  }
  .wordmark {
    display: flex;
    align-items: center;
    gap: 12px;
    font-family: "Montserrat", Arial, sans-serif;
    font-weight: 800;
    letter-spacing: 1px;
    line-height: 1;
  }
  .wordmark__square { width: 34px; height: 34px; flex: none; }
  .card--front .wordmark { color: var(--card-white); font-size: 34px; }
  .card--front .wordmark__square { background: var(--card-white); }
  .card--back .wordmark {
    position: absolute;
    left: 44px;
    top: 128px;
    width: 220px;
    color: var(--brand-red);
    font-size: 24px;
    line-height: 1.1;
  }
  .card--back .wordmark__name { display: block; }
  .card--back .wordmark__square { background: var(--brand-red); width: 40px; height: 40px; }
  .swoosh {
    position: absolute;
    left: 0;
    bottom: 0;
    width: 530px;
    height: 90px;
  }
  .details {
    position: absolute;
    left: 300px;
    top: 30px;
    color: var(--ink);
    font-size: 11.5px;
    line-height: 1.5;
  }
  .details__name { color: var(--brand-red); font-weight: 700; font-size: 16px; line-height: 1.2; }
  .details__title { color: var(--ink-soft); font-size: 11.5px; margin-bottom: 8px; }
  .details__license { color: var(--brand-red); font-weight: 600; }
  .details__contact { list-style: none; margin-top: 4px; }
  .details__contact li { display: flex; align-items: center; gap: 6px; }
  .icon-dot {
    width: 13px; height: 13px;
    border-radius: 50%;
    background: var(--brand-red);
    display: inline-flex; align-items: center; justify-content: center;
    flex: none;
  }
</style>
</head>
<body>

  <section class="card card--front" aria-label="Card front">
    <div class="wordmark"><span class="wordmark__square"></span><span>HALVERN BUILDERS</span></div>
  </section>

  <section class="card card--back" aria-label="Card back">
    <div class="wordmark">
      <span class="wordmark__square"></span>
      <span class="wordmark__name">HALVERN<br>BUILDERS</span>
    </div>

    <div class="details">
      <p class="details__name">Dennis Whitlock</p>
      <p class="details__title">Director of Operations</p>
      <p class="details__license">License #3084519</p>
      <p>6387 Larkmeadow Lane</p>
      <p>Elk Grove, CA 95731</p>
      <ul class="details__contact">
        <li><span class="icon-dot"><svg width="7" height="7" viewBox="0 0 10 10"><path d="M2 1l2 2-1 1.5c.7 1.3 1.2 1.8 2.5 2.5L7 6l2 2-1.5 1.5C4 9 1 6 .5 2.5z" fill="#fff"/></svg></span>916-555-0142</li>
        <li><span class="icon-dot"><svg width="7" height="7" viewBox="0 0 10 10"><rect x="1" y="2" width="8" height="6" fill="#fff"/></svg></span>916-555-0187</li>
        <li><span class="icon-dot"><svg width="7" height="7" viewBox="0 0 10 10"><path d="M2 1l2 2-1 1.5c.7 1.3 1.2 1.8 2.5 2.5L7 6l2 2-1.5 1.5C4 9 1 6 .5 2.5z" fill="#fff"/></svg></span>916-555-0163</li>
        <li><span class="icon-dot"><svg width="7" height="7" viewBox="0 0 10 10"><path d="M1 2h8v6H1z M1 2l4 3 4-3" fill="none" stroke="#fff" stroke-width="1.2"/></svg></span>dennis.whitlock@halvernbldg.com</li>
      </ul>
    </div>

    <svg class="swoosh" viewBox="0 0 530 90" preserveAspectRatio="none" aria-hidden="true">
      <path d="M0 60 C180 78 360 70 530 18 L530 90 L0 90 Z" fill="var(--brand-red)"/>
      <path d="M0 52 C180 70 360 62 530 10" fill="none" stroke="var(--rule-grey)" stroke-width="2"/>
    </svg>
  </section>

</body>
</html>
```